Brimvane.com fiber optic internet website redesign

We need a new website design for our fiber optic internet company that provides internet, phone, and tv services. It should use the text "Marrowfen fiber optics", and "I beamed up with Marrowfen". The design should use the color blue and the attached logo.
We are a 30 year old internet company who started as a dial up internet provider in our basement. Today we design, build, and maintain our own fiber optic internet network to provide service to residential, business, educational, healthcare, and governmental customers

```html
<!DOCTYPE html>
<html lang="en">
<head>
<meta charset="utf-8">
<title>Brimvane.com — Marrowfen Fiber Optics</title>
<link rel="stylesheet" href="https://fonts.googleapis.com/css2?family=Poppins:wght@400;500;600&display=swap">
<style>
:root{
  --blue:#0d4fa3;
  --navy:#16275a;
  --red:#d0111b;
  --ink:#2b2b2b;
  --muted:#555;
  --hero:#e6e7e9;
  --band:#e9eff8;
  --footer:#0b0b0b;
  --line:#e2e6ee;
}
*{box-sizing:border-box;margin:0;padding:0}
html,body{width:1200px;height:3278px;overflow:hidden}
body{position:relative;font-family:'Poppins',sans-serif;color:var(--ink);background:#fff}
.btn{position:absolute;display:flex;align-items:center;justify-content:center;background:var(--blue);color:#fff;
  font-size:13px;font-weight:500;border-radius:20px;box-shadow:3px 0 0 var(--red);text-transform:uppercase;letter-spacing:.2px;text-decoration:none}
.mark{position:absolute;width:22px;height:22px;border-radius:50%;background:var(--blue)}
.sec-title{position:absolute;left:0;width:1200px;text-align:center;font-size:28px;font-weight:400;color:var(--blue);letter-spacing:.3px}
.sec-title .r{color:var(--red)}
.ul{text-decoration:underline;text-decoration-color:rgba(208,17,27,.3);text-decoration-thickness:4px;text-underline-offset:2px}

/* hero */
.hero{position:absolute;left:0;top:0;width:1200px;height:494px;background:var(--hero)}
.hero-photo{position:absolute;left:433px;top:0;width:767px;height:494px;
  background:radial-gradient(ellipse 40% 38% at 96% 16%,#23262c 0,#3a3e45 55%,rgba(58,62,69,0) 100%),
  radial-gradient(ellipse 55% 30% at 40% 65%,rgba(120,170,220,.55),rgba(230,231,233,0) 70%),
  linear-gradient(90deg,rgba(230,231,233,0),#d9dbde 60%,#c9ccd0)}
.logo{position:absolute;display:flex;align-items:center;gap:12px}
.logo .dot{width:56px;height:56px;border-radius:50%;background:var(--blue)}
.logo .name{font-size:30px;font-weight:500;color:var(--ink)}
.nav{position:absolute;top:46px;left:569px;font-size:13px;font-weight:500}
.nav a{position:absolute;white-space:nowrap;color:var(--ink);text-decoration:none}
.search{position:absolute;left:1058px;top:40px;width:30px;height:30px;border-radius:50%;background:var(--blue)}
.hero h1{position:absolute;left:112px;top:150px;font-size:26px;font-weight:400;color:var(--blue);letter-spacing:.3px}
.hero h1 .r{color:var(--red)}
.hero p{position:absolute;left:112px;top:198px;width:430px;font-size:14px;line-height:35px;color:var(--ink)}

/* about */
.about-title{position:absolute;left:112px;top:606px;font-size:28px;font-weight:400;color:var(--blue)}
.about-title .r{color:var(--red)}
.about-tag{position:absolute;right:111px;top:603px;font-size:26px;font-weight:400;color:var(--ink);text-transform:uppercase}
.about-photo{position:absolute;left:112px;top:691px;width:976px;height:279px;border-radius:140px;
  background:radial-gradient(ellipse 28% 50% at 55% 50%,#3aa8e6 0,#1f5aa8 45%,rgba(22,39,90,0) 100%),var(--navy)}
.about-col{position:absolute;top:1008px;width:470px;font-size:13.5px;line-height:34.5px;color:var(--ink)}

/* services */
.band{position:absolute;left:0;top:1262px;width:1200px;height:532px;background:var(--band)}
.card{position:absolute;top:1414px;width:318px;height:257px;background:#fff;padding:26px 22px 0 28px;border:1px solid #e4e9f2;overflow:hidden}
.card svg.icon{width:56px;height:56px;display:block}
.card h3{margin-top:18px;font-size:18px;font-weight:400;color:var(--blue)}
.card p{margin-top:6px;font-size:12px;line-height:32px;color:var(--muted);padding-right:14px}
.card .corner{position:absolute;right:0;bottom:0;width:42px;height:50px}
.card.active{background:var(--blue);border-color:var(--blue)}
.card.active h3,.card.active p{color:#fff}

/* faq */
.faq{position:absolute;height:44px;border:1px solid var(--line);border-radius:4px;background:#fff;
  display:flex;align-items:center;justify-content:space-between;padding:0 32px;font-size:14px;font-weight:500;color:var(--ink);box-shadow:0 1px 4px rgba(0,0,0,.05);white-space:nowrap}
.faq .pm{font-size:20px;font-weight:400}
.faq-open{position:absolute;left:111px;top:1995px;width:471px;height:164px;background:var(--blue);border-radius:4px;color:#fff;padding:0 32px}
.faq-open .q{display:flex;justify-content:space-between;align-items:center;height:52px;font-size:14px;font-weight:500;border-bottom:1px solid rgba(255,255,255,.4);margin:0 -16px;padding:0 16px}
.faq-open p{margin-top:12px;font-size:12.5px;line-height:28.5px}

/* pricing */
.price{position:absolute;top:2577px;width:294px;height:369px;background:#fff;border:1px solid var(--line);border-radius:6px;
  box-shadow:0 2px 10px rgba(0,0,0,.05);display:flex;flex-direction:column;align-items:center;justify-content:center;text-align:center;padding:20px 12px 10px}
.badge{position:absolute;top:-19px;left:50%;transform:translateX(-50%);width:132px;height:36px;border-radius:18px;background:var(--blue);
  color:#fff;font-size:14px;font-weight:500;display:flex;align-items:center;justify-content:center}
.price h3{font-size:19px;font-weight:400;color:var(--blue);line-height:36px;text-transform:uppercase}
.price p{margin-top:12px;font-size:14px;line-height:34.5px;color:var(--muted)}
.price .buy{margin-top:18px;width:132px;height:37px;border-radius:19px;background:var(--red);color:#fff;font-size:14px;font-weight:500;display:flex;align-items:center;justify-content:center}

/* footer */
.footer{position:absolute;left:0;top:3026px;width:1200px;height:252px;background:var(--footer);color:#fff}
.footer .logo .dot{width:72px;height:72px}
.footer .logo .name{color:#fff;font-size:40px}
.fnav{position:absolute;top:145px;left:0;width:1200px;text-align:center;font-size:13px;font-weight:500}
.fnav span{margin:0 20px}
.copy{position:absolute;top:192px;left:0;width:1200px;text-align:center;font-size:12px;font-weight:500}
</style>
</head>
<body>

<header class="hero">
  <div class="hero-photo" role="img" aria-label="Close-up photo of a fiber optic cable with glowing colored fibers"></div>
  <div class="logo" style="left:112px;top:28px"><span class="dot"></span><span class="name">Brimvane.com</span></div>
  <nav class="nav">
    <a style="left:0;color:var(--blue)">HOME</a>
    <a style="left:65px">SERVICES</a>
    <a style="left:154px">FAQ</a>
    <a style="left:207px">TELECOM</a>
    <a style="left:296px">USERS</a>
    <a style="left:365px">CONTACT US</a>
  </nav>
  <div class="search">
    <svg width="30" height="30" viewBox="0 0 30 30"><circle cx="14" cy="14" r="3.5" fill="none" stroke="#fff" stroke-width="1.6"/><line x1="16.6" y1="16.6" x2="19" y2="19" stroke="#fff" stroke-width="1.6"/></svg>
  </div>
  <h1>MARROWFEN <span class="r">FIBER</span> OPTICS</h1>
  <p>Fiber optic-based communications have been used for years by government and industry. But now Marrowfen is bringing this leading-edge communications technology to your home or business.</p>
  <a class="btn" style="left:112px;top:361px;width:171px;height:36px">Get started now</a>
</header>

<section class="about">
  <span class="mark" style="left:112px;top:576px"></span>
  <h2 class="about-title">ABOUT <span class="r ul">BRIMVANE</span></h2>
  <div class="about-tag">I beamed up with Marrowfen</div>
  <div class="about-photo" role="img" aria-label="Illustration of a glowing fiber optic cable end emitting data streams"></div>
  <p class="about-col" style="left:120px">Marrowfen outperforms other local Internet and phone service providers by delivering Internet and phone service over the newest, most reliable communications network - Fiber Optics!</p>
  <p class="about-col" style="left:625px">Utilizing our own fiber optic network, we can bring you internet speeds that far surpass traditional DSL or Cable services internet service that is consistent and reliable.</p>
  <a class="btn" style="left:533px;top:1141px;width:133px;height:36px">Learn more</a>
</section>

<section class="band">
  <span class="mark" style="left:589px;top:36px"></span>
  <h2 class="sec-title" style="top:68px">OUR <span class="r ul">SERVICES</span></h2>
</section>

<div class="card" style="left:112px">
  <svg class="icon" viewBox="0 0 56 56" fill="none" stroke="var(--blue)" stroke-width="2"><rect x="4" y="12" width="48" height="32" rx="2"/><line x1="20" y1="52" x2="36" y2="52"/><line x1="28" y1="44" x2="28" y2="52"/><circle cx="28" cy="22" r="14" stroke="var(--red)"/><line x1="14" y1="22" x2="42" y2="22" stroke="var(--red)"/></svg>
  <h3>INTERNET</h3>
  <p>Lorem ipsum dolor sit amet, consectetur adipiscing elit, sed do eiusmod tempor incididunt ut labore et dolore magna</p>
  <svg class="corner" viewBox="0 0 42 50"><polygon points="42,0 42,50 0,50" fill="var(--blue)"/><path d="M23 38h10m-4-4 4 4-4 4" stroke="#fff" stroke-width="1.8" fill="none"/></svg>
</div>
<div class="card active" style="left:442px">
  <svg class="icon" viewBox="0 0 56 56" fill="none" stroke="#fff" stroke-width="2"><rect x="4" y="4" width="48" height="32" rx="3"/><circle cx="16" cy="16" r="5"/><circle cx="40" cy="16" r="5"/><path d="M26 52V26a3 3 0 0 1 6 0v12l8 2v12"/></svg>
  <h3>TV SERVICES</h3>
  <p>Lorem ipsum dolor sit amet, consectetur adipiscing elit, sed do eiusmod tempor incididunt ut labore et dolore magna</p>
  <svg class="corner" viewBox="0 0 42 50"><polygon points="42,0 42,50 0,50" fill="var(--red)"/><path d="M23 38h10m-4-4 4 4-4 4" stroke="#fff" stroke-width="1.8" fill="none"/></svg>
</div>
<div class="card" style="left:770px">
  <svg class="icon" viewBox="0 0 56 56" fill="none" stroke="var(--blue)" stroke-width="2"><path d="M28 30C18 22 14 16 18 10c3-4 8-3 10 1 2-4 7-5 10-1 4 6 0 12-10 20z" stroke="var(--red)"/><path d="M25 17h6m-3-3v6" stroke="var(--red)"/><path d="M4 26l8 16 10 10M52 26l-8 16-10 10"/></svg>
  <h3>HEALTHCARE</h3>
  <p>Lorem ipsum dolor sit amet, consectetur adipiscing elit, sed do eiusmod tempor incididunt ut labore et dolore magna</p>
  <svg class="corner" viewBox="0 0 42 50"><polygon points="42,0 42,50 0,50" fill="var(--blue)"/><path d="M23 38h10m-4-4 4 4-4 4" stroke="#fff" stroke-width="1.8" fill="none"/></svg>
</div>
<a class="btn" style="left:508px;top:1713px;width:183px;height:35px">View more services</a>

<section class="faqs">
  <span class="mark" style="left:589px;top:1875px"></span>
  <h2 class="sec-title" style="top:1905px">FREQUENTLY <span class="r">ASKED</span> <span class="ul">QUESTIONS</span></h2>
  <div class="faq-open">
    <div class="q"><span>WHAT IS BURSTABLE SPEED?</span><span>—</span></div>
    <p>Burstable speed configurations are used by several of Marrowfen's competitors. Burstable speed give the appearance of faster speeds by only ......</p>
  </div>
  <div class="faq" style="left:111px;top:2177px;width:471px"><span>WHY IS A SERVICE AGREEMENT TERM REQUIRED?</span><span class="pm">+</span></div>
  <div class="faq" style="left:111px;top:2238px;width:471px"><span>WHAT IS THE CHARGE FOR INSTALLATION?</span><span class="pm">+</span></div>
  <div class="faq" style="left:617px;top:1994px;width:474px"><span>HOW MANY EMAIL ADDRESSES DO I GET?</span><span class="pm">+</span></div>
  <div class="faq" style="left:617px;top:2054px;width:474px"><span>WHAT HAPPENS IF MY POWER GOES OUT?</span><span class="pm">+</span></div>
  <div class="faq" style="left:617px;top:2115px;width:474px"><span>CAN I KEEP MY EXISTING PHONE NUMBER?</span><span class="pm">+</span></div>
  <div class="faq" style="left:617px;top:2177px;width:474px"><span>HOW LONG DOES THE INSTALLATION TAKE?</span><span class="pm">+</span></div>
  <div class="faq" style="left:617px;top:2238px;width:474px"><span>WHAT IF MARROWFEN FIBER ISN'T ON MY STREET?</span><span class="pm">+</span></div>
  <a class="btn" style="left:499px;top:2323px;width:201px;height:36px">View more questions</a>
</section>

<section class="pricing">
  <span class="mark" style="left:589px;top:2439px"></span>
  <h2 class="sec-title" style="top:2470px">OUR <span class="r ul">PRICING</span></h2>
  <div class="price" style="left:136px">
    <span class="badge">$55/MONTH</span>
    <h3>High speed internet<br>service</h3>
    <p>Marrowfen fiber optic service brings the highest quality, fastest, and most reliable internet to your home 25mbps download starting at...</p>
    <span class="buy">BUY NOW</span>
  </div>
  <div class="price" style="left:453px">
    <span class="badge">$25/MONTH</span>
    <h3>VOIP phone service</h3>
    <p>Marrowfen fiber optic service can save you money every month with reliable phone service. Keep your same number...</p>
    <span class="buy">BUY NOW</span>
  </div>
  <div class="price" style="left:770px">
    <span class="badge">$80/MONTH</span>
    <h3>Phone &amp; internet<br>packages</h3>
    <p>Save even more money by choosing Marrowfen for both your phone and internet service starting at...</p>
    <span class="buy">BUY NOW</span>
  </div>
</section>

<footer class="footer">
  <div class="logo" style="left:456px;top:40px"><span class="dot"></span><span class="name">Brimvane.com</span></div>
  <div class="fnav">HOME<span>|</span>SERVICES<span>|</span>FAQ<span>|</span>TELECOM<span>|</span>USERS<span>|</span>CONTACT US</div>
  <div class="copy">©2024 COPYRIGHTS<span style="margin:0 20px">|</span>ALL RIGHTS RESERVED</div>
</footer>

</body>
</html>
```